Business Card Design

Vintage looking Hair Salon, where the customer service is 100%. We are based in a cottage. With shabby chic console tables and beautiful ornate mirrors..and rich brown leather cutting chairs. Chandeliers at the window, and a ornate patchwork sofa.
our clientele are 28years upwards.. Mums with small children.. Ladies that lunch, and men that want more than a barbers and are prepared to pay for our services.
I am looking for a classy business card.. That look expensive.. Where our initials WMP become a visual reference.. I was thinking of cream card initials in black on a embossed tarnished silver.. But I'm open to suggestion. I want,  need the design to be able to work with flyers price list ect.

Industry/Entity Type
Business
Contact Information for Business Card
Willow Mane Parlour
17 Fernbrook Lane
Dunmore Green
bN42 6QW
FB thewillowmaneparlour
Info@thewilowmaneparlour.co.uk
0208 761 5924

```html
<!DOCTYPE html>
<html lang="en">
<head>
<meta charset="utf-8">
<title>Willow Mane Parlour – Business Cards</title>
<link rel="stylesheet" href="https://fonts.googleapis.com/css2?family=Didact+Gothic&family=Crimson+Text:wght@600&display=swap">
<style>
  :root {
    --backdrop: #b3aea6;
    --card: #ffffff;
    --card-edge: #3a3a3a;
    --ink-sans: #a9a898;
    --ink-serif: #a6a6a6;
    --ornament: #cfcfcf;
    --rule: #b0b0b0;
  }
  html, body { margin: 0; padding: 0; overflow: hidden; }
  body {
    width: 1200px; height: 900px;
    background: var(--backdrop);
    position: relative;
  }
  .card {
    position: absolute;
    background: var(--card);
    border: 1px solid var(--card-edge);
    box-sizing: border-box;
  }
  .card--landscape { left: 80px; top: 235px; width: 567px; height: 354px; font-family: "Didact Gothic", sans-serif; color: var(--ink-sans); }
  .card--portrait { left: 745px; top: 148px; width: 355px; height: 566px; font-family: "Crimson Text", serif; font-weight: 600; color: var(--ink-serif); }

  .line {
    position: absolute; left: 0; right: 0;
    text-align: center; height: 30px; line-height: 30px;
    margin: 0; white-space: nowrap;
  }
  .card--landscape .line { font-size: 18px; }
  .card--portrait .line { font-size: 15.5px; }
  .card--landscape .monogram { font-size: 36px; height: 44px; line-height: 44px; letter-spacing: 2px; }
  .card--portrait .monogram { font-size: 38px; height: 44px; line-height: 44px; letter-spacing: 2px; }
  .card--portrait .business-name { font-size: 21px; }

  .rule {
    position: absolute; left: 106px; width: 142px;
    height: 0; border-top: 1px solid var(--rule);
  }
  .ornament {
    position: absolute;
    background: var(--ornament);
    border-radius: 10px;
  }
</style>
</head>
<body>

<section class="card card--landscape" aria-label="Landscape business card">
  <div class="ornament" role="img" aria-label="Ornate antler corner flourish, top left" style="left:27px; top:15px; width:90px; height:160px;"></div>
  <div class="ornament" role="img" aria-label="Ornate antler corner flourish, bottom left" style="left:27px; top:180px; width:90px; height:160px;"></div>
  <div class="ornament" role="img" aria-label="Ornate antler corner flourish, top right" style="left:448px; top:15px; width:92px; height:160px;"></div>
  <div class="ornament" role="img" aria-label="Ornate antler corner flourish, bottom right" style="left:448px; top:180px; width:92px; height:160px;"></div>

  <p class="line monogram" style="top:15px;">WMP</p>
  <p class="line" style="top:90px;">Willow Mane Parlour</p>
  <p class="line" style="top:120px;">17 Fernbrook Lane</p>
  <p class="line" style="top:150px;">Dunmore Green bN42 6QW FB</p>
  <p class="line" style="top:210px;">www.thewillowmaneparlour.co.uk</p>
  <p class="line" style="top:240px;">Info@thewilowmaneparlour.co.uk</p>
  <p class="line" style="top:308px;">0208 761 5924</p>
</section>

<section class="card card--portrait" aria-label="Portrait business card">
  <div class="ornament" role="img" aria-label="Ornate antler corner flourish, top left" style="left:28px; top:40px; width:42px; height:162px;"></div>
  <div class="ornament" role="img" aria-label="Ornate antler corner flourish, top right" style="left:285px; top:40px; width:42px; height:162px;"></div>
  <div class="ornament" role="img" aria-label="Ornate antler corner flourish, bottom left" style="left:28px; top:370px; width:42px; height:167px;"></div>
  <div class="ornament" role="img" aria-label="Ornate antler corner flourish, bottom right" style="left:285px; top:370px; width:42px; height:167px;"></div>

  <p class="line monogram" style="top:38px;">WMP</p>
  <p class="line business-name" style="top:112px;">Willow Mane Parlour</p>
  <div class="rule" style="top:225px;"></div>
  <p class="line" style="top:247px;">www.thewillowmaneparlour.co.uk</p>
  <p class="line" style="top:277px;">Info@thewilowmaneparlour.co.uk</p>
  <div class="rule" style="top:335px;"></div>
  <p class="line" style="top:397px;">17 Fernbrook Lane</p>
  <p class="line" style="top:422px;">Dunmore Green bN42 6QW FB</p>
  <p class="line" style="top:499px;">0208 761 5924</p>
</section>

</body>
</html>
```